Real Estate Investor needs awesome business card design

I invest in real estate, focused on multi-family properties, and I need a business card to hand out to potential partners. I prefer simple, clean designs, but it needs to stand out, so I'd like there to be a bit of red in the design as well.

It should include this information:

Front
Dallin Pecksworth
Real Estate Investor
Direct phone: 502-867-3394
Email: dallinhpecksworth@quillmail.example
Headshot (Picture), I've uploaded a few, just pick the one you think looks best with your design. You can remove the background from the headshot image if it looks better.

Back
The back of the card's design should flow and be congruent with the front. On the back I want to put an inspirational quote or question. There will be different ones depending on the card, so I'll need the original file so I can edit it in the end.

For now, use “The Pessimist Sees Difficulty In Every Opportunity. The Optimist Sees The Opportunity In Every Difficulty.” -Barnaby Ellsworth

Target Market(s)

Investors

Industry/Entity Type

Real Estate

Contact Information for Business Card

Front
Dallin Pecksworth
Real Estate Investor

Back
The back of the card's design should flow and be congruent with the front. On the back I want to put an inspirational quote or question. There will be different ones depending on the card, so I'll need the original file so I can edit it in the end. I've uploaded some EXAMPLES of business cards with quotes on them. Don't copy but feel free to use them as inspiration.

The design will be printed on "ZIB sized" business cards
1039 x 697 pixels
with rounded corners

Font styles to use
Serif
Decorative
Script

Colors
ec1f27

Requirements
Must have
• Headshot, name, and other information in it.
• 1039 x 697 pixels
• Rounded corners
• Clean design that pops. I'm open to see any color background, including black.
• Headshots can be located here: https://www.filecrate.example/sh/8kd2wq7mzt31hvx/BBQTXP4ruf9LmQ0KhcvWx7b?dl=0
Nice to have
• It would be awesome if the design included a personal signature or monogram, but if not I'll get a personal logo developed later and the card redesigned if I think it needs it.
Should not have
• Cluttered design

```html
<!DOCTYPE html>
<html lang="en">
<head>
<meta charset="utf-8">
<title>Dallin Pecksworth — Business Card</title>
<link rel="stylesheet" href="https://fonts.googleapis.com/css2?family=Open+Sans:wght@400;700&family=Roboto+Condensed:wght@700&family=Tinos:ital@1&display=swap">
<style>
  :root {
    --navy: #1f2d55;
    --red: #e41e2b;
    --ink: #2b2b2b;
    --white: #ffffff;
    --page: #ededed;
    --silver-light: #f8f8f8;
    --silver-mid: #dcdddf;
    --silver-dark: #c3c4c7;
  }
  html, body {
    margin: 0;
    padding: 0;
    width: 1000px;
    height: 1200px;
    overflow: hidden;
    background: var(--page);
  }
  .sheet {
    position: relative;
    width: 1000px;
    height: 1200px;
  }
  .card {
    position: absolute;
    left: 100px;
    width: 800px;
    height: 480px;
    filter: drop-shadow(0 6px 10px rgba(0, 0, 0, 0.25));
  }
  .card--front { top: 100px; }
  .card--back { top: 620px; }
  .card svg { display: block; }
  .name {
    font-family: "Open Sans", Arial, sans-serif;
    font-weight: 700;
    font-size: 25px;
    letter-spacing: 1px;
    fill: var(--ink);
  }
  .role {
    font-family: "Open Sans", Arial, sans-serif;
    font-weight: 400;
    font-size: 23px;
    fill: var(--ink);
  }
  .contact {
    font-family: "Open Sans", Arial, sans-serif;
    font-weight: 400;
    font-size: 24px;
    fill: var(--white);
  }
  .contact-icon {
    fill: none;
    stroke: var(--white);
    stroke-width: 1.8;
  }
  .quote-line {
    font-family: "Roboto Condensed", "Arial Narrow", sans-serif;
    font-weight: 700;
    font-size: 32px;
    fill: var(--navy);
  }
  .quote-line--accent {
    font-size: 34px;
    fill: var(--red);
  }
  .quote-mark {
    font-family: "Roboto Condensed", "Arial Narrow", sans-serif;
    font-weight: 700;
    font-size: 64px;
    fill: var(--navy);
  }
  .quote-author {
    font-family: "Tinos", "Times New Roman", serif;
    font-style: italic;
    font-size: 31px;
    fill: var(--white);
  }
</style>
</head>
<body>
<main class="sheet">

  <!-- Front of card -->
  <section class="card card--front" aria-label="Business card front">
    <svg width="800" height="480" viewBox="0 0 800 480">
      <defs>
        <linearGradient id="silver-face" x1="0" y1="0" x2="1" y2="0">
          <stop offset="0" stop-color="var(--silver-dark)"/>
          <stop offset="0.45" stop-color="var(--silver-light)"/>
          <stop offset="1" stop-color="var(--silver-dark)"/>
        </linearGradient>
        <linearGradient id="silver-band" x1="0" y1="0" x2="1" y2="0">
          <stop offset="0" stop-color="#9fa1a5"/>
          <stop offset="0.5" stop-color="#ffffff"/>
          <stop offset="1" stop-color="#a7a9ad"/>
        </linearGradient>
        <linearGradient id="headshot-tones" x1="0" y1="0" x2="0" y2="1">
          <stop offset="0" stop-color="#e4e4e4"/>
          <stop offset="0.35" stop-color="#d9b39c"/>
          <stop offset="0.7" stop-color="#b5847a"/>
          <stop offset="1" stop-color="#7b3445"/>
        </linearGradient>
        <clipPath id="front-shape">
          <rect x="0" y="0" width="800" height="480" rx="36" ry="36"/>
        </clipPath>
      </defs>
      <g clip-path="url(#front-shape)">
        <rect class="card-face" x="0" y="0" width="800" height="480" fill="url(#silver-face)"/>
        <g class="headshot" role="img" aria-label="Headshot photo of Dallin Pecksworth">
          <rect x="0" y="0" width="274" height="390" fill="url(#headshot-tones)"/>
        </g>
        <path class="wave-band" d="M0,352 C250,330 450,258 800,247 L800,268 C460,278 250,352 0,376 Z" fill="url(#silver-band)"/>
        <path class="wave-accent" d="M0,350 C250,328 450,256 800,245" fill="none" stroke="var(--red)" stroke-width="5"/>
        <path class="wave-base" d="M0,374 C250,350 460,276 800,266 L800,480 L0,480 Z" fill="var(--navy)"/>

        <text class="name" x="298" y="178">DALLIN PECKSWORTH</text>
        <text class="role" x="298" y="212">Real Estate Investor</text>

        <g class="contact-phone">
          <rect class="contact-icon" x="298" y="338" width="13" height="22" rx="2.5"/>
          <line class="contact-icon" x1="302" y1="355" x2="307" y2="355"/>
          <text class="contact" x="336" y="358">502-867-3394</text>
        </g>
        <g class="contact-email">
          <rect class="contact-icon" x="296" y="386" width="20" height="14" rx="1.5"/>
          <polyline class="contact-icon" points="296,387 306,395 316,387"/>
          <text class="contact" x="336" y="400">dallinhpecksworth@quillmail.example</text>
        </g>
      </g>
    </svg>
  </section>

  <!-- Back of card -->
  <section class="card card--back" aria-label="Business card back">
    <svg width="800" height="480" viewBox="0 0 800 480">
      <defs>
        <linearGradient id="silver-face-back" x1="0" y1="0" x2="1" y2="0">
          <stop offset="0" stop-color="var(--silver-dark)"/>
          <stop offset="0.5" stop-color="var(--silver-light)"/>
          <stop offset="1" stop-color="var(--silver-dark)"/>
        </linearGradient>
        <linearGradient id="silver-band-back" x1="0" y1="0" x2="1" y2="0">
          <stop offset="0" stop-color="#a7a9ad"/>
          <stop offset="0.5" stop-color="#ffffff"/>
          <stop offset="1" stop-color="#9fa1a5"/>
        </linearGradient>
        <clipPath id="back-shape">
          <rect x="0" y="0" width="800" height="480" rx="36" ry="36"/>
        </clipPath>
      </defs>
      <g clip-path="url(#back-shape)">
        <rect class="card-face" x="0" y="0" width="800" height="480" fill="url(#silver-face-back)"/>

        <text class="quote-mark" x="58" y="130">“</text>
        <text class="quote-line" x="93" y="117" textLength="586" lengthAdjust="spacing">THE PESSIMIST SEES DIFFICULTY</text>
        <text class="quote-line quote-line--accent" x="93" y="175" textLength="592" lengthAdjust="spacing">IN EVERY OPPORTUNITY.</text>
        <text class="quote-line" x="93" y="225" textLength="586" lengthAdjust="spacing">THE OPTIMIST SEES THE OPPORTUNITY</text>
        <text class="quote-line quote-line--accent" x="93" y="279" textLength="572" lengthAdjust="spacing">IN EVERY DIFFICULTY</text>
        <text class="quote-mark" x="680" y="292">”</text>

        <path class="wave-band" d="M0,306 C250,320 550,388 800,418 L800,440 C550,412 250,342 0,328 Z" fill="url(#silver-band-back)"/>
        <path class="wave-accent" d="M0,304 C250,318 550,386 800,416" fill="none" stroke="var(--red)" stroke-width="5"/>
        <path class="wave-base" d="M0,326 C250,340 550,410 800,440 L800,480 L0,480 Z" fill="var(--navy)"/>

        <text class="quote-author" x="98" y="405">Barnaby Ellsworth</text>
      </g>
    </svg>
  </section>

</main>
</body>
</html>
```